Wealth Education Business Needs Sharp Business Card Design

We need a business card design for a recently launched investor education business called Harbor Crest.

The final design should promote security, empowerment, self improvement and financial gain. The card will ideally promote the stature of the business.

For more information and colours please visit harborcrest.com.au

Target Market(s)

Corporate executives and high net worth individuals

Industry/Entity Type

Education

Contact Information for Business Card

Name
Position
Contact Address
Phone
Mobile
Email
Website

```html
<!DOCTYPE html>
<html lang="en">
<head>
<meta charset="utf-8">
<title>Harbor Crest Business Card</title>
<link rel="stylesheet" href="https://fonts.googleapis.com/css2?family=Mulish:wght@400;500;700&display=swap">
<style>
  :root {
    --backdrop: #e8e5e1;
    --card-navy: #1f2a3d;
    --fold-line: #172032;
    --ink-white: #ffffff;
    --ink-soft: #e6e9ee;
    --accent-teal: #1d9a9d;
    --accent-sky: #3a9fd6;
    --shadow: rgba(20, 24, 32, 0.28);
  }
  * { margin: 0; padding: 0; box-sizing: border-box; }
  html, body {
    width: 1200px; height: 1000px; overflow: hidden;
    background: var(--backdrop);
    font-family: "Mulish", "Helvetica Neue", Arial, sans-serif;
  }
  .canvas { position: relative; width: 1200px; height: 1000px; }
  .card {
    position: absolute; left: 265px; width: 665px; height: 397px;
    background: var(--card-navy);
    box-shadow: 0 6px 18px var(--shadow);
  }
  .card--front { top: 73px; }
  .card--back { top: 532px; }

  .fold { position: absolute; left: 362px; top: 0; bottom: 0; width: 2px; background: var(--fold-line); }

  .wordmark {
    position: absolute; color: var(--ink-white);
    font-weight: 500; letter-spacing: 0.12em; text-transform: uppercase; white-space: nowrap;
  }
  .card--front .wordmark { left: 40px; top: 180px; font-size: 27px; }
  .card--back .lockup {
    position: absolute; left: 0; right: 0; top: 170px; text-align: center;
  }
  .card--back .wordmark { position: static; display: block; font-size: 40px; line-height: 48px; }
  .tagline {
    display: block; margin-top: 10px; color: var(--accent-sky);
    font-size: 15px; letter-spacing: 0.28em; text-transform: uppercase;
  }

  .contact { position: absolute; left: 389px; top: 104px; color: var(--ink-soft); font-size: 16px; line-height: 20px; }
  .contact__name { color: var(--accent-teal); font-weight: 700; font-size: 18px; }
  .contact__role { margin-bottom: 22px; }
  .contact__address { margin-bottom: 8px; }
  .contact__list { list-style: none; }
  .contact__list li { display: flex; align-items: center; gap: 6px; height: 19.5px; }
  .contact__list svg { width: 13px; height: 13px; fill: var(--accent-teal); flex: none; }
</style>
</head>
<body>
<main class="canvas">
  <section class="card card--front">
    <div class="wordmark">Harbor Crest</div>
    <div class="fold"></div>
    <div class="contact">
      <div class="contact__name">Daniel Whitford</div>
      <div class="contact__role">Founder / CEO</div>
      <div class="contact__address">14 Ridgeview Lane<br>Ashford VIC 3190</div>
      <ul class="contact__list">
        <li><svg viewBox="0 0 13 13"><path d="M4 0.5h5a1 1 0 0 1 1 1v10a1 1 0 0 1-1 1H4a1 1 0 0 1-1-1v-10a1 1 0 0 1 1-1zm0.6 1.3v8.2h3.8V1.8z"/></svg>999 999 9999</li>
        <li><svg viewBox="0 0 13 13"><path d="M1 4.5c0-1.5 2.5-2.5 5.5-2.5S12 3 12 4.5v1H9.5V4.2h-6v1.3H1zM3.5 6h6l2 5H1.5z"/></svg>999 999 9999</li>
        <li><svg viewBox="0 0 13 13"><path d="M1 3h11v7H1zm1 1v.4l4.5 3 4.5-3V4z"/></svg>info@harborcrest.com.au</li>
        <li><svg viewBox="0 0 13 13"><path d="M6.5 1a5.5 5.5 0 1 0 0 11 5.5 5.5 0 0 0 0-11zm0 1.2c.6.7 1.1 2 1.2 3.6H5.3c.1-1.6.6-2.9 1.2-3.6zM4.2 5.8H2.3a4.3 4.3 0 0 1 2.6-3.3c-.4.9-.7 2-.7 3.3zm0 1.2c0 1.3.3 2.4.7 3.3a4.3 4.3 0 0 1-2.6-3.3zm1.1 0h2.4c-.1 1.6-.6 2.9-1.2 3.6-.6-.7-1.1-2-1.2-3.6zm3.5 0h1.9a4.3 4.3 0 0 1-2.6 3.3c.4-.9.7-2 .7-3.3zm0-1.2c0-1.3-.3-2.4-.7-3.3a4.3 4.3 0 0 1 2.6 3.3z"/></svg>www.harborcrest.com.au</li>
      </ul>
    </div>
  </section>

  <section class="card card--back">
    <div class="lockup">
      <span class="wordmark">Harbor Crest</span>
      <span class="tagline">Study Build Thrive</span>
    </div>
  </section>
</main>
</body>
</html>
```